Vocational Mentor needs an impressive business card

1. I need a business card (or maybe three with identic look) to promote me and my three business titles/services:
- Vocational Mentor. I help people find their vocation and live happily from it. I use my 20 years of experience in business, management and psychology to help them identify the most efficient ways to make a living doing what they are passionate about.
- Business Angel. I help founders start a succesful business with minimum risks and costs. I use my 20 years of experience in sales, management and entrepreneurship to help them identify the most efficient ways, in terms of time and cost, to validate their business idea.
- Learning Designer. I design unique learning programs that produce long-term cognitive and behavioural changes to people and organisations. I use my 20 years of experience in learning, teaching and change management to create minimalist experiences and processes that allow them to change efficiently in their pursued direction.

2. I would like a two-sided business card, on the front with my name, contact details and titles, on the back the explanation of the services.
Updates

Hi all,

I updated my brief, included contacts info and give feedback on all designs I got. I am new on this platform so please tell me if you need anything else or if I don't use corectly the platform forms.

Kind regards,
Tudor

Hi all,

I shortened the services description by deleting the phrase "I call..."

Kind regards,
Tudor

Target Market(s)

Freelancers, startups, people and organization willing to invest in change through ultimate learning experiences

Industry/Entity Type

Business

Font styles to use
Serif

Requirements
Must have
• Front side: full name, titles, web site, email, phone like below:
Tudor Vasilache
Vocational Mentor, Business Angel, Learning Designer
info@tudorvasilache.example
www.tudorvasilache.example
+40-745-TUDORV
Nice to have
• Back side: the description of the services I provide as in the task description.
1/3: it would be nice if I can jam all three titles on the front side but then I need a solution to jam all three services on the back side.

```html
<!DOCTYPE html>
<html lang="en">
<head>
<meta charset="utf-8">
<title>Tudor Vasilache — Business Card</title>
<link href="https://fonts.googleapis.com/css2?family=Mulish:wght@300;400;800&display=swap" rel="stylesheet">
<style>
  :root{
    --backdrop:#2b2b2d;
    --card:#4e5864;
    --band-top:#5a6878;
    --band-mid:#4f5761;
    --band-low:#3d4a56;
    --green:#8cc63f;
    --yellow:#f2e21b;
    --orange:#f26a21;
    --white:#f4f4f4;
    --muted:#9aa3ad;
    --mint:#a9e0d8;
  }
  *{box-sizing:border-box;margin:0;padding:0}
  html,body{width:1200px;height:1200px;overflow:hidden;background:var(--backdrop)}
  body{font-family:"Mulish",sans-serif;position:relative}

  .card{position:absolute;left:150px;width:900px;height:514px;box-shadow:0 18px 40px rgba(0,0,0,.55);overflow:hidden}
  .card--front{top:50px;background:var(--card)}
  .card--back{top:630px;display:flex;flex-direction:column}

  .accent{position:absolute;width:170px;height:8px;background:var(--green);border-radius:4px}
  .accent--top{top:26px;right:-20px}
  .accent--bottom{bottom:26px;left:-20px}

  .identity{position:absolute;left:70px;top:200px;width:370px;text-align:right}
  .identity__name{font-weight:300;font-size:34px;letter-spacing:1px;color:var(--white);text-transform:uppercase;margin-bottom:10px}
  .identity__title{font-weight:300;font-size:29px;line-height:1.05}
  .identity__title--mentor{color:var(--green)}
  .identity__title--angel{color:var(--yellow)}
  .identity__title--designer{color:var(--orange)}

  .divider{position:absolute;left:470px;top:160px;height:220px;border-left:2px dotted rgba(255,255,255,.35)}

  .contacts{position:absolute;left:500px;top:215px;list-style:none;color:var(--white);font-weight:300;font-size:21px;line-height:1.45}

  .service{flex:1;display:flex;flex-direction:column;align-items:center;justify-content:center;padding:0 40px;text-align:center}
  .service--mentor{background:var(--band-top)}
  .service--angel{background:var(--band-mid)}
  .service--designer{background:var(--band-low)}
  .service__heading{font-weight:800;font-size:22px;text-transform:uppercase;letter-spacing:.5px;margin-bottom:6px}
  .service--mentor .service__heading{color:var(--green)}
  .service--angel .service__heading{color:var(--yellow)}
  .service--designer .service__heading{color:var(--orange)}
  .service__text{font-weight:400;font-size:14.5px;line-height:1.3;color:var(--muted)}
  .service--designer .service__text{color:var(--mint)}
</style>
</head>
<body>
  <section class="card card--front" aria-label="Business card front">
    <span class="accent accent--top"></span>
    <span class="accent accent--bottom"></span>
    <div class="identity">
      <h1 class="identity__name">Tudor Vasilache</h1>
      <p class="identity__title identity__title--mentor">Vocational Mentor</p>
      <p class="identity__title identity__title--angel">Business Angel</p>
      <p class="identity__title identity__title--designer">Learning Designer</p>
    </div>
    <span class="divider"></span>
    <ul class="contacts">
      <li>phone: +40-745-TUDORV</li>
      <li>email: info@tudorvasilache.example</li>
      <li>site: www.tudorvasilache.example</li>
    </ul>
  </section>

  <section class="card card--back" aria-label="Business card back">
    <article class="service service--mentor">
      <h2 class="service__heading">Vocational Mentor</h2>
      <p class="service__text">I help people find their vocation and live happily from it. I use my 20 years of experience in business, management and psychology to help them identify the most efficient ways to make a living doing what they are passionate about.</p>
    </article>
    <article class="service service--angel">
      <h2 class="service__heading">Business Angel</h2>
      <p class="service__text">I help founders start a succesful business with minimum risks and costs. I use my 20 years of experience in sales, management and entrepreneurship to help them identify the most efficient ways, in terms of time and cost, to validate their business idea.</p>
    </article>
    <article class="service service--designer">
      <h2 class="service__heading">Learning Designer</h2>
      <p class="service__text">I design unique learning programs that produce long-term cognitive and behavioural changes to people and organisations. I use my 20 years of experience in learning, teaching and change management to create minimalist experiences and processes that allow them to change efficiently in their pursued direction.</p>
    </article>
  </section>
</body>
</html>
```